Social Media Cover and Profile

We already have our own logo. We just need a fresh design on our social media pages. We are not happy with our current designs. We would like to incorporate our YIKE billboard and the colors are blue (#05143f) and white. You can also incorporate silver as well. We are a family law office (Divorce and Custody) We no longer want to incorporate the Spire of Dunvale photo that we are currently using. You can look at our Facebook page; The Law Office of Miles T. Hadley.

Target Market(s)

Potential Clients

Industry/Entity Type

Family Law

Logo Text

Our Logo Is The Law Office of Miles T. Hadley with the Sheild

Requirements
Must have
• Text to include:
Central Pennslyvania's Premier Family Law Firm

Ability to be resized to and used as all images in social media, including but not limited to: Youtube Channel art, Facebook Cover and Profile.
Nice to have
• Darker color but we are open to "bright" ideas.

```html
<!DOCTYPE html>
<html lang="en">
<head>
<meta charset="utf-8">
<title>Central Pennsylvania's Premier Family Law Firm</title>
<link href="https://fonts.googleapis.com/css2?family=Poppins:wght@500;700&display=swap" rel="stylesheet">
<style>
  :root {
    --navy-deep: #05143f;
    --navy: #1c2b5c;
    --navy-soft: #2a3a6c;
    --white: #ffffff;
    --photo-light: #d9d4cc;
    --photo-warm: #b9a894;
    --photo-dark: #5b4a3c;
  }
  html, body {
    margin: 0;
    padding: 0;
    overflow: hidden;
    background: var(--navy-deep);
  }
  .cover {
    position: relative;
    width: 1200px;
    height: 457px;
    overflow: hidden;
    background: linear-gradient(90deg, var(--navy) 0%, var(--navy) 40%, var(--navy-soft) 60%, var(--navy) 100%);
    font-family: "Poppins", sans-serif;
    color: var(--white);
  }
  .cover__backdrop {
    position: absolute;
    inset: 0;
    background: linear-gradient(90deg, rgba(28,43,92,0) 25%, rgba(60,74,120,0.55) 35%, rgba(28,43,92,0.2) 50%, rgba(28,43,92,0) 100%);
  }
  .cover__art {
    position: absolute;
    inset: 0;
    width: 1200px;
    height: 457px;
  }
  .headline {
    position: absolute;
    left: 50px;
    top: 48px;
    margin: 0;
  }
  .headline__kicker {
    display: block;
    font-weight: 500;
    font-size: 23px;
    line-height: 33px;
  }
  .headline__title {
    display: block;
    margin-top: 18px;
    font-weight: 700;
    font-size: 66px;
    line-height: 100px;
    letter-spacing: 0.5px;
  }
</style>
</head>
<body>
  <div class="cover">
    <div class="cover__backdrop" role="img" aria-label="Faint, darkened photo of a family home interior behind the navy background"></div>

    <svg class="cover__art" viewBox="0 0 1200 457" xmlns="http://www.w3.org/2000/svg">
      <defs>
        <linearGradient id="photo-tones" x1="0" y1="0" x2="1" y2="1">
          <stop offset="0" stop-color="var(--photo-light)"/>
          <stop offset="0.45" stop-color="var(--photo-warm)"/>
          <stop offset="0.75" stop-color="var(--photo-light)"/>
          <stop offset="1" stop-color="var(--photo-dark)"/>
        </linearGradient>
      </defs>
      <polygon class="photo-frame" fill="var(--white)"
        points="383,59 553,0 1017,0 1178,351 1131,457 521,457"/>
      <polygon class="photo-window" fill="url(#photo-tones)" role="img"
        aria-label="Photo of a father kneeling in a home doorway hugging his young daughter, a suitcase beside them"
        points="398,66 589,0 1004,0 1163,349 1118,457 533,457"/>
    </svg>

    <h1 class="headline">
      <span class="headline__kicker">Central Pennslyvania's<br>Premier</span>
      <span class="headline__title">Family<br>Law Firm</span>
    </h1>
  </div>
</body>
</html>
```